we need a homepage for a marketplace

We manage all projects using our ground-breaking platform Velbrim Portal. You get access to 150+ partners in 70 countries, security, cost efficiency, technical skills, speed, 100% visibility and accountability.Velbrim aims to help clients realize the full potential of their investments, provide a competitive price, establish the business need as a competitive advantage, and provide a strategic business asset that can facilitate growth.
Target Market(s)
Freelancers
Industry/Entity Type
Business Software
Number of Pages Required
1 page
Requirements
Must have
- Credentials -http://qlvtk.com/freelancer/public
- Front :
- Client:
- Email id - doriek@fallowquartzsystems.com
- Password - 123456
- Partner:
- Email id - mortenl@fallowquartzsystems.com
- Password - 123456
- Project Manager:
- Email id - lorcan@fallowquartzsystems.com
- Password - 123456
Nice to have
- It will be nice to have a creative design, and a outside the box look/feel

```html
<!DOCTYPE html>
<html lang="en">
<head>
<meta charset="utf-8">
<title>Velbrim – Project Marketplace</title>
<link href="https://fonts.googleapis.com/css2?family=Roboto+Slab:wght@400;700&family=Open+Sans:wght@400;600;700&display=swap" rel="stylesheet">
<style>
:root{
  --ink:#2a2a2a;
  --muted:#777;
  --line:#dcdcdc;
  --teal:#3f8c98;
  --teal-dark:#2f6f7a;
  --orange:#e8582a;
  --dark:#2c2c2c;
  --footer:#2f3437;
  --footer-deep:#25292b;
  --light:#ececec;
  --white:#fff;
}
*{box-sizing:border-box;margin:0;padding:0}
html,body{width:1200px;height:4088px;overflow:hidden}
body{font-family:"Open Sans",Arial,sans-serif;color:var(--ink);background:var(--white);position:relative}
.slab{font-family:"Roboto Slab",Georgia,serif}
section,header,footer{position:absolute;left:0;width:1200px;overflow:hidden}

/* header */
.site-header{top:0;height:64px;background:var(--white);border-bottom:1px solid var(--line)}
.brand{position:absolute;left:40px;top:16px;font-family:"Roboto Slab",serif;font-weight:700;font-size:26px;color:var(--ink);display:flex;align-items:center;gap:8px}
.brand .dot{width:12px;height:12px;background:var(--teal);border-radius:50%}
.main-nav{position:absolute;left:450px;top:24px;display:flex;gap:28px;font-size:12px;font-weight:600;letter-spacing:.5px}
.header-actions{position:absolute;right:40px;top:18px;display:flex;gap:10px}
.btn-outline{border:1px solid #999;font-size:11px;font-weight:700;padding:6px 12px;color:var(--ink)}

/* hero */
.hero{top:64px;height:676px}
.hero-photo{position:absolute;inset:0;background:linear-gradient(120deg,#7a6f6a 0%,#4a3e44 35%,#2a2430 65%,#3b3340 100%)}
.hero-title{position:absolute;left:360px;top:300px;width:560px;text-align:center;color:var(--white);font-family:"Roboto Slab",serif;font-weight:700;font-size:38px;line-height:1.3}
.hero-actions{position:absolute;left:100px;top:592px;display:flex;gap:20px}
.btn{display:inline-flex;align-items:center;gap:10px;color:var(--white);font-size:13px;font-weight:700;letter-spacing:.5px;padding:0 22px;height:52px}
.btn-teal{background:var(--teal)}
.btn-orange{background:var(--orange)}
.btn .ic{width:22px;height:22px;border-radius:50%;background:rgba(255,255,255,.9)}
.hero-cut{position:absolute;left:0;bottom:0}

/* how it works */
.how{top:740px;height:588px;background:var(--white)}
.section-title{font-family:"Roboto Slab",serif;font-weight:700;font-size:30px;text-transform:uppercase}
.how .section-title{position:absolute;left:72px;top:20px}
.how .sub{position:absolute;left:72px;top:68px;font-size:14px;color:var(--muted)}
.steps{position:absolute;left:72px;top:130px;display:flex;gap:20px}
.step{width:249px;height:400px;border:1px solid var(--line);background:var(--white)}
.step-art{height:190px;margin:20px 20px 0}
.step-arrow{margin:14px 20px 0;width:30px;height:30px}
.step h3{margin:8px 20px 0;font-size:17px;font-weight:700;text-transform:uppercase;line-height:1.2}
.step p{margin:10px 20px 0;font-size:12px;color:var(--muted);line-height:1.5}

/* services */
.services{top:1328px;height:732px;background:var(--dark);color:var(--white)}
.services .section-title{position:absolute;left:72px;top:60px;width:820px;line-height:1.35}
.service-grid{position:absolute;left:72px;top:220px;display:grid;grid-template-columns:repeat(4,246px);column-gap:24px;row-gap:56px}
.service .icon{width:46px;height:46px}
.service h4{margin-top:14px;font-size:17px;font-weight:700;text-transform:uppercase;line-height:1.2;height:42px}
.service p{margin-top:10px;font-size:12px;color:#b9b9b9;line-height:1.55}

/* about */
.about{top:2060px;height:600px}
.about-photo{position:absolute;inset:0;background:linear-gradient(100deg,#5a4a40 0%,#8b7562 40%,#c4b7a8 70%,#9aa7b0 100%)}
.about-card{position:absolute;left:72px;top:150px;width:320px;height:300px;background:rgba(20,20,20,.78);color:var(--white);padding:30px 28px}
.about-card h2{font-family:"Roboto Slab",serif;font-size:28px;font-weight:400;text-transform:uppercase;text-align:center}
.about-card p{margin-top:18px;font-family:"Roboto Slab",serif;font-size:16px;line-height:1.5;text-align:center}
.about-card .learn{display:block;width:120px;margin:22px auto 0;border:1px solid var(--white);text-align:center;font-size:13px;padding:8px 0}

/* top talent */
.talent{top:2660px;height:240px;background:var(--light);text-align:center}
.talent .section-title{margin-top:46px;font-size:28px}
.talent p{margin-top:12px;font-size:14px;color:#555}
.talent .btn{margin-top:26px;height:48px}

/* partners */
.partners{top:2900px;height:600px;background:var(--white)}
.partners .section-title{position:absolute;left:0;width:1200px;top:54px;text-align:center;font-size:28px}
.partner-row{position:absolute;left:72px;top:200px;display:flex;gap:24px}
.partner{width:246px;height:290px;border:1px solid var(--line);padding:12px}
.partner .photo{height:160px;background:linear-gradient(160deg,#d8dde2,#8e9aa6)}
.partner dl{margin-top:12px;font-size:12px;line-height:1.6;color:#444}
.pager{position:absolute;left:560px;top:530px;display:flex;gap:8px}
.pager span{width:32px;height:32px;border:1px solid #888;display:flex;align-items:center;justify-content:center}

/* newsletter */
.newsletter{top:3500px;height:120px;background:var(--teal-dark);color:var(--white)}
.newsletter h2{position:absolute;left:72px;top:24px;font-family:"Roboto Slab",serif;font-size:24px;line-height:1.2;font-weight:400}
.newsletter p{position:absolute;left:316px;top:22px;width:640px;font-size:12px;line-height:1.5}
.newsletter form{position:absolute;left:316px;top:66px;display:flex;gap:10px}
.newsletter .field{width:280px;height:34px;background:var(--white);color:#888;font-size:12px;padding:9px 12px}
.newsletter .submit{width:200px;height:34px;background:#1f4a52;font-size:12px;font-weight:700;text-align:center;padding-top:9px;letter-spacing:1px}

/* footer */
.site-footer{top:3620px;height:468px;background:var(--footer);color:#cfd3d5}
.footer-cols{position:absolute;left:72px;top:40px;display:flex;gap:60px}
.footer-col{width:160px}
.footer-col h5{color:var(--white);font-size:14px;font-weight:700;margin-bottom:10px}
.footer-col li{list-style:none;font-size:12px;line-height:1.7}
.footer-col h5.second{margin-top:14px}
.social{position:absolute;right:72px;top:40px;display:flex;gap:8px}
.social span{width:30px;height:30px;border:1px solid #9aa1a4;border-radius:50%}
.contact{position:absolute;right:72px;top:120px;display:flex;gap:30px;font-size:12px}
.footer-brand{position:absolute;right:72px;top:320px;font-family:"Roboto Slab",serif;font-weight:700;font-size:46px;color:var(--white);display:flex;align-items:center;gap:12px}
.footer-brand .dot{width:18px;height:18px;border-radius:50%;background:var(--teal)}
.footer-bar{position:absolute;left:0;bottom:0;width:1200px;height:44px;background:var(--footer-deep);font-size:12px;padding:14px 72px;color:#aab0b3}
</style>
</head>
<body>

<header class="site-header">
  <div class="brand"><span>Velbrim</span><span class="dot"></span></div>
  <nav class="main-nav"><span>ABOUT US</span><span>HOW IT WORKS</span><span>BROWSE PROJECT MANAGER</span></nav>
  <div class="header-actions"><span class="btn-outline">LOGIN</span><span class="btn-outline">ADD PROJECT</span></div>
</header>

<section class="hero">
  <div class="hero-photo" role="img" aria-label="Photo of hands holding a tablet at a desk, dark purple tones"></div>
  <h1 class="hero-title">Aiming To Provide Faster, Smarter And Cheaper Solutions And Services Assuring Rapid Growth Of</h1>
  <div class="hero-actions">
    <span class="btn btn-teal"><span class="ic"></span>BECOME A PARTNER</span>
    <span class="btn btn-orange"><span class="ic"></span>POST YOUR PROJECT</span>
  </div>
  <svg class="hero-cut" width="1200" height="140" viewBox="0 0 1200 140">
    <polygon points="0,140 0,110 420,120 1200,40 1200,140" fill="#fff"/>
    <polygon points="1040,140 1200,70 1200,140" fill="#e6e6e6"/>
  </svg>
</section>

<section class="how">
  <h2 class="section-title">How It Works</h2>
  <p class="sub">Organizations Can Benefit From Our Talent Pool In The Following Easy Steps</p>
  <div class="steps">
    <article class="step">
      <div class="step-art" role="img" aria-label="Illustration of a project being posted" style="background:linear-gradient(135deg,#fde3d8,#f6b49b)"></div>
      <svg class="step-arrow" viewBox="0 0 30 30"><circle cx="15" cy="15" r="14" fill="none" stroke="#e8582a" stroke-width="2"/><path d="M10 15h10M16 11l4 4-4 4" stroke="#e8582a" stroke-width="2" fill="none"/></svg>
      <h3 style="color:var(--orange)">Post Your Project</h3>
      <p>Lorem ipsum dolor sit amet, consectetuer adipiscing elit, sed diam nonummy nibh euismod tincidunt</p>
    </article>
    <article class="step">
      <div class="step-art" role="img" aria-label="Illustration of choosing an expert" style="background:linear-gradient(135deg,#dff1f3,#9fd0d6)"></div>
      <svg class="step-arrow" viewBox="0 0 30 30"><circle cx="15" cy="15" r="14" fill="none" stroke="#3f8c98" stroke-width="2"/><path d="M10 15h10M16 11l4 4-4 4" stroke="#3f8c98" stroke-width="2" fill="none"/></svg>
      <h3 style="color:var(--teal)">Select An Expert</h3>
      <p>Lorem ipsum dolor sit amet, consectetuer adipiscing elit, sed diam nonummy nibh euismod tincidunt</p>
    </article>
    <article class="step">
      <div class="step-art" role="img" aria-label="Illustration of work on a laptop" style="background:linear-gradient(135deg,#ece3f3,#b9a6cf)"></div>
      <svg class="step-arrow" viewBox="0 0 30 30"><circle cx="15" cy="15" r="14" fill="none" stroke="#e8582a" stroke-width="2"/><path d="M10 15h10M16 11l4 4-4 4" stroke="#e8582a" stroke-width="2" fill="none"/></svg>
      <h3 style="color:var(--orange)">Work On The Project</h3>
      <p>Lorem ipsum dolor sit amet, consectetuer adipiscing elit, sed diam nonummy nibh euismod tincidunt</p>
    </article>
    <article class="step">
      <div class="step-art" role="img" aria-label="Illustration of a payment on completion" style="background:linear-gradient(135deg,#e4f3dc,#a9d696)"></div>
      <svg class="step-arrow" viewBox="0 0 30 30"><circle cx="15" cy="15" r="14" fill="none" stroke="#3f8c98" stroke-width="2"/><path d="M10 15h10M16 11l4 4-4 4" stroke="#3f8c98" stroke-width="2" fill="none"/></svg>
      <h3 style="color:var(--teal)">Pay Only When Satisfied</h3>
      <p>Lorem ipsum dolor sit amet, consectetuer adipiscing elit, sed diam nonummy nibh euismod tincidunt</p>
    </article>
  </div>
</section>

<section class="services">
  <h2 class="section-title">Project Manager For Every Business Challenge Across A Wide Range Of Industries</h2>
  <div class="service-grid">
    <div class="service"><svg class="icon" viewBox="0 0 46 46"><circle cx="23" cy="23" r="22" fill="#4a4a4a"/><path d="M14 28a6 6 0 0 1 2-11 8 8 0 0 1 15 1 5 5 0 0 1 0 10z" fill="#fff"/></svg><h4>Cloud Computing</h4><p>Move your systems to the cloud and access your data from anywhere with secure, scalable hosting.</p></div>
    <div class="service"><svg class="icon" viewBox="0 0 46 46"><circle cx="23" cy="23" r="22" fill="#4a4a4a"/><path d="M15 23l6 6 11-12" stroke="#fff" stroke-width="3" fill="none"/></svg><h4>QA Testing</h4><p>We help you find and eliminate defects early, so every release ships stable and reliable.</p></div>
    <div class="service"><svg class="icon" viewBox="0 0 46 46"><circle cx="23" cy="23" r="22" fill="#4a4a4a"/><circle cx="23" cy="19" r="5" fill="#fff"/><path d="M14 33a9 7 0 0 1 18 0z" fill="#fff"/></svg><h4>Consulting Services</h4><p>Expert guidance on planning, budgeting and delivery to match technology with business goals.</p></div>
    <div class="service"><svg class="icon" viewBox="0 0 46 46"><circle cx="23" cy="23" r="22" fill="#4a4a4a"/><path d="M18 17l-6 6 6 6M28 17l6 6-6 6" stroke="#fff" stroke-width="3" fill="none"/></svg><h4>Web Development</h4><p>Robust, fast and secure web applications built on modern frameworks by vetted developers.</p></div>
    <div class="service"><svg class="icon" viewBox="0 0 46 46"><circle cx="23" cy="23" r="22" fill="#4a4a4a"/><rect x="13" y="15" width="20" height="15" fill="none" stroke="#fff" stroke-width="2"/><path d="M19 34h8" stroke="#fff" stroke-width="2"/></svg><h4>Web Design</h4><p>Clean, user friendly interfaces that turn visitors into loyal customers across all devices.</p></div>
    <div class="service"><svg class="icon" viewBox="0 0 46 46"><circle cx="23" cy="23" r="22" fill="#4a4a4a"/><path d="M23 12l9 4v7c0 6-4 10-9 12-5-2-9-6-9-12v-7z" fill="#fff"/></svg><h4>Security &amp; Compliance</h4><p>Protect your business with audits, strong policies and standards that keep data safe.</p></div>
    <div class="service"><svg class="icon" viewBox="0 0 46 46"><circle cx="23" cy="23" r="22" fill="#4a4a4a"/><rect x="17" y="11" width="12" height="24" rx="2" fill="none" stroke="#fff" stroke-width="2"/><circle cx="23" cy="31" r="1.5" fill="#fff"/></svg><h4>Mobile App Development</h4><p>Native and cross platform apps designed, built and launched by proven mobile teams.</p></div>
    <div class="service"><svg class="icon" viewBox="0 0 46 46"><circle cx="23" cy="23" r="22" fill="#4a4a4a"/><path d="M13 25v-3a10 10 0 0 1 20 0v3" stroke="#fff" stroke-width="2" fill="none"/><rect x="11" y="24" width="5" height="8" fill="#fff"/><rect x="30" y="24" width="5" height="8" fill="#fff"/></svg><h4>Technical Support Services</h4><p>Round the clock help desk and maintenance that keeps your systems running smoothly.</p></div>
  </div>
</section>

<section class="about">
  <div class="about-photo" role="img" aria-label="Photo of a smiling developer at a laptop in a bright office"></div>
  <div class="about-card">
    <h2>About Velbrim</h2>
    <p>We are experienced and highly qualified software engineers, cloud architects, inventors, cyber security engineers and project managers.</p>
    <span class="learn">Learn More</span>
  </div>
</section>

<section class="talent">
  <h2 class="section-title">Top Talent At Your Disposal</h2>
  <p>Lorem ipsum dolor sit amet, consectetuer adipiscing elit, sed diam nonummy nibh euismod tincidunt ut laoreet</p>
  <span class="btn btn-teal"><span class="ic"></span>REGISTER AS A BUSINESS PARTNER</span>
</section>

<section class="partners">
  <h2 class="section-title">Our Top Partners</h2>
  <div class="partner-row">
    <div class="partner"><div class="photo" role="img" aria-label="Portrait photo of a partner"></div><dl><dt>Name : Marisol</dt><dd>Education : MBA</dd><dd>Companies Worked For : NA</dd><dd>Notes : NA</dd></dl></div>
    <div class="partner"><div class="photo" role="img" aria-label="Portrait photo of a partner"></div><dl><dt>Name : Marisol</dt><dd>Education : MBA</dd><dd>Companies Worked For : NA</dd><dd>Notes : NA</dd></dl></div>
    <div class="partner"><div class="photo" role="img" aria-label="Portrait photo of a partner"></div><dl><dt>Name : Marisol</dt><dd>Education : MBA</dd><dd>Companies Worked For : NA</dd><dd>Notes : NA</dd></dl></div>
    <div class="partner"><div class="photo" role="img" aria-label="Portrait photo of a partner"></div><dl><dt>Name : Marisol</dt><dd>Education : MBA</dd><dd>Companies Worked For : NA</dd><dd>Notes : NA</dd></dl></div>
  </div>
  <div class="pager">
    <span><svg width="12" height="12" viewBox="0 0 12 12"><path d="M8 2L4 6l4 4" stroke="#333" stroke-width="2" fill="none"/></svg></span>
    <span><svg width="12" height="12" viewBox="0 0 12 12"><path d="M4 2l4 4-4 4" stroke="#333" stroke-width="2" fill="none"/></svg></span>
  </div>
</section>

<section class="newsletter">
  <h2>SUBSCRIBE<br>NEWSLETTER</h2>
  <p>Get a weekly round up of the top cloud computing news and views from Velbrim. It's quick and easy to help you stay ahead with smarter decisions.</p>
  <form>
    <span class="field">Enter Your Name</span>
    <span class="field">Enter Your Email</span>
    <span class="submit">SUBSCRIBE</span>
  </form>
</section>

<footer class="site-footer">
  <div class="footer-cols">
    <div class="footer-col"><h5>Industries</h5><ul><li>Financial Services</li><li>Retail</li><li>Healthcare</li><li>Education</li><li>Manufacturing</li><li>Media</li><li>Real Estate</li><li>Logistics</li><li>Telecom</li></ul></div>
    <div class="footer-col"><h5>Project Category</h5><ul><li>Cloud Computing</li><li>QA Testing</li><li>Consulting Services</li><li>Web Development</li><li>Web Design</li><li>Security &amp; Compliance</li><li>Mobile App Development</li><li>Technical Support Services</li></ul></div>
    <div class="footer-col"><h5>Support &amp; Downloads</h5><ul><li>Support Home</li><li>Support Center</li><li>Help</li><li>FAQ</li><li>Downloads</li></ul><h5 class="second">Events</h5><ul><li>Latest</li><li>Upcoming</li></ul></div>
    <div class="footer-col"><h5>Career</h5><ul><li>Internship</li><li>Openings</li></ul><h5 class="second">Other</h5><ul><li>About</li><li>News Room</li><li>Sitemap</li></ul></div>
  </div>
  <div class="social"><span></span><span></span><span></span><span></span></div>
  <div class="contact"><span>Customer Service</span><span>hello@velbrim.com</span><span>(020) 555 0148</span></div>
  <div class="footer-brand"><span>Velbrim</span><span class="dot"></span></div>
  <div class="footer-bar">© 2018 Velbrim. All Rights Reserved. &nbsp;Terms of Use &nbsp;|&nbsp; Privacy Policy</div>
</footer>

</body>
</html>
```